Marisol business card and stationary
business card and stationary
Marisol business card and stationary - Retailers
Creative Brief
Bright & Fun-filled
Janet Wroblenko
owner, designer
marisol a florist 418 north brook lane Fairview, NC 28730
info@marisolblooms.example
marisolblooms.example
Concepts
Stationery for Online Retailer

```html
<!DOCTYPE html>
<html lang="en">
<head>
<meta charset="utf-8">
<title>Marisol a florist – business card</title>
<link href="https://fonts.googleapis.com/css2?family=Questrial&display=swap" rel="stylesheet">
<style>
  :root {
    --backdrop: #7d7d7d;
    --pink: #ee6a7c;
    --pink-deep: #e2506a;
    --pink-soft: #f8b3bd;
    --blush: #fde6e8;
    --green: #8a9a3c;
    --ink: #555555;
    --white: #ffffff;
  }
  * { margin: 0; padding: 0; box-sizing: border-box; }
  html, body { width: 1200px; height: 901px; overflow: hidden; }
  body {
    background: var(--backdrop);
    font-family: "Questrial", "Century Gothic", sans-serif;
    display: flex;
    align-items: center;
    justify-content: center;
    gap: 50px;
  }
  .card {
    position: relative;
    width: 540px;
    height: 309px;
    overflow: hidden;
    box-shadow: 0 10px 24px rgba(0,0,0,.35);
  }
  /* front */
  .card-front {
    background: radial-gradient(circle at 35% 40%, var(--pink-soft) 0%, var(--pink) 55%, var(--pink-deep) 100%);
  }
  .card-front .brand {
    position: absolute;
    right: 48px;
    top: 128px;
    font-size: 44px;
    color: var(--white);
    letter-spacing: 1px;
  }
  /* back */
  .card-back {
    background: linear-gradient(170deg, var(--white) 40%, var(--blush) 75%, var(--pink-soft) 100%);
  }
  .card-back .bands { position: absolute; left: 0; top: 0; width: 540px; height: 110px; }
  .contact-person { position: absolute; left: 34px; top: 122px; color: var(--ink); }
  .person-name { color: var(--pink-deep); font-size: 17px; }
  .person-role { font-size: 11px; margin-top: 2px; }
  .address { font-size: 11px; line-height: 1.45; margin-top: 20px; }
  .brand-block {
    position: absolute;
    right: 40px;
    top: 150px;
    display: flex;
    align-items: center;
    gap: 10px;
  }
  .brand-dot { width: 18px; height: 18px; border-radius: 50%; background: var(--pink); }
  .brand-block .brand { font-size: 38px; color: var(--ink); }
  .contact-lines {
    position: absolute;
    left: 262px;
    top: 228px;
    list-style: none;
    font-size: 11px;
    color: var(--ink);
    line-height: 1.5;
  }
  .contact-lines li { display: flex; align-items: center; gap: 7px; white-space: nowrap; }
  .contact-lines svg { width: 10px; height: 10px; fill: var(--green); flex: none; }
</style>
</head>
<body>

<section class="card card-front" aria-label="Business card front">
  <span class="brand">marisol</span>
</section>

<section class="card card-back" aria-label="Business card back">
  <svg class="bands" viewBox="0 0 540 110" preserveAspectRatio="none" aria-hidden="true">
    <path d="M0 0 H540 V46 C420 18 250 28 0 78 Z" fill="var(--pink)"/>
    <path d="M0 78 C250 28 420 18 540 46 V62 C420 40 250 48 0 96 Z" fill="var(--green)"/>
    <path d="M0 96 C250 48 420 40 540 62 V70 C420 50 250 60 0 106 Z" fill="var(--pink-soft)"/>
  </svg>

  <div class="contact-person">
    <p class="person-name">Janet Wroblenko</p>
    <p class="person-role">Owner | Designer</p>
    <p class="address">Marisol a florist<br>418 North Brook Lane<br>Fairview, NC 28730</p>
  </div>

  <div class="brand-block">
    <span class="brand-dot"></span>
    <span class="brand">marisol</span>
  </div>

  <ul class="contact-lines">
    <li><svg viewBox="0 0 10 10"><path d="M2 0.5 L3.6 0.5 L4.2 2.8 L3 3.6 C3.6 5 5 6.4 6.4 7 L7.2 5.8 L9.5 6.4 L9.5 8 C9.5 9 8.5 9.5 7.5 9.5 C4 9 1 6 0.5 2.5 C0.5 1.5 1 0.5 2 0.5 Z"/></svg>704.555.0148</li>
    <li><svg viewBox="0 0 10 10"><path d="M0.5 2 H9.5 V8 H0.5 Z M0.5 2 L5 5.5 L9.5 2" fill="none" stroke="var(--green)" stroke-width="1.2"/></svg>info@marisolblooms.example</li>
    <li><svg viewBox="0 0 10 10"><circle cx="5" cy="5" r="4.4" fill="none" stroke="var(--green)" stroke-width="1.1"/><path d="M0.6 5 H9.4 M5 0.6 C2.5 3 2.5 7 5 9.4 M5 0.6 C7.5 3 7.5 7 5 9.4" fill="none" stroke="var(--green)" stroke-width="0.9"/></svg>marisolblooms.example</li>
  </ul>
</section>

</body>
</html>
```